Business Card Design Project

We need a Business Card for an Mechanical Engineering firm in Singapore. The design should be Modern & Technical looking, yet eye catching.

Our company deals in Cutting Tools & Machine Accessories for the Manufacturing Industries such as Oil & Gas, Aero Space, etc... For more information on our Company, you can either email me or view our website www.valtrion.com.sg.

We are trying to revamp our image to give our consumers a fresh new perspective to our company, so we welcome all ideas.

Industry/Entity Type

Business

Requirements
Must have
• Must incorporate New Company Logo into the card as shown in Uploaded file.

```html
<!DOCTYPE html>
<html lang="en">
<head>
<meta charset="utf-8">
<title>Valtrion Tools – Business Card</title>
<link rel="stylesheet" href="https://fonts.googleapis.com/css2?family=Roboto:wght@300;400&display=swap">
<style>
  :root {
    --page: #ffffff;
    --slate-center: #8d9c9b;
    --slate-edge: #56635f;
    --panel-top: #262d31;
    --panel-bottom: #4b5659;
    --crimson: #8c1838;
    --white: #ffffff;
    --soft-white: #e6eaea;
  }
  * { margin: 0; padding: 0; box-sizing: border-box; }
  html, body {
    width: 827px; height: 1200px; overflow: hidden;
    background: var(--page);
    font-family: "Roboto", Arial, sans-serif;
  }
  .sheet { position: relative; width: 827px; height: 1200px; }

  .card {
    position: absolute; left: 28px; width: 769px; height: 468px;
    background: radial-gradient(ellipse 60% 70% at 50% 45%, var(--slate-center), var(--slate-edge));
    overflow: hidden;
  }
  .card--front { top: 60px; }
  .card--back { top: 628px; background: radial-gradient(ellipse 55% 65% at 60% 40%, var(--slate-center), var(--slate-edge)); }

  .brand {
    position: absolute; left: 0; right: 0; top: 208px;
    display: flex; justify-content: center; align-items: center; gap: 16px;
  }
  .brand__dot { width: 26px; height: 26px; border-radius: 50%; background: var(--crimson); }
  .brand__name {
    font-weight: 400; font-size: 44px; letter-spacing: 2px;
    color: var(--crimson); line-height: 1;
  }

  .products-panel {
    position: absolute; left: 0; top: 0; width: 322px; height: 468px;
    background: linear-gradient(180deg, var(--panel-top), var(--panel-bottom));
    color: var(--white);
  }
  .products-panel__title {
    position: absolute; left: 33px; top: 33px;
    font-size: 17px; font-weight: 400;
  }
  .products-list {
    position: absolute; left: 33px; top: 72px; list-style: none;
    font-size: 16px; font-weight: 300; line-height: 21.8px; color: var(--soft-white);
  }
  .company {
    position: absolute; left: 33px; top: 342px;
    font-size: 19px; line-height: 25px;
  }
  .company__name { font-weight: 400; }
  .company__address { font-weight: 300; font-style: normal; color: var(--soft-white); }

  .contact {
    position: absolute; left: 384px; top: 110px; color: var(--white);
  }
  .contact__name { font-size: 26px; font-weight: 400; color: var(--crimson); margin-bottom: 12px; }
  .contact__line { font-size: 21px; font-weight: 400; line-height: 29px; }
  .contact__value { font-weight: 300; color: var(--soft-white); }

  .website {
    position: absolute; left: 437px; top: 424px;
    font-size: 22px; font-weight: 300; color: var(--crimson);
  }
</style>
</head>
<body>
<main class="sheet">
  <section class="card card--front" aria-label="Card front">
    <div class="brand">
      <span class="brand__dot"></span>
      <span class="brand__name">VALTRION TOOLS</span>
    </div>
  </section>

  <section class="card card--back" aria-label="Card back">
    <div class="products-panel">
      <h2 class="products-panel__title">OUR PRODUCTS</h2>
      <ul class="products-list">
        <li>- Arden-Kessler</li>
        <li>- Brask</li>
        <li>- Holloway</li>
        <li>- Flex-Run</li>
        <li>- Torv</li>
        <li>- Graffel</li>
        <li>- Lind Metall</li>
        <li>- Strandmeier</li>
      </ul>
      <div class="company">
        <p class="company__name">Valtrion Tools Pte Ltd</p>
        <address class="company__address">27 Kallang Crescent #03-08,<br>Meridian Industrial Hub,<br>Singapore 339412</address>
      </div>
    </div>

    <div class="contact">
      <p class="contact__name">Marissa</p>
      <p class="contact__line">Phone <span class="contact__value">65-61234570</span></p>
      <p class="contact__line">Email <span class="contact__value">hello@valtrion.com.sg</span></p>
    </div>

    <p class="website">http://www.valtrion.com.sg</p>
  </section>
</main>
</body>
</html>
```